A new Blog: Turning Over New Leaves

I need a wordpress blog design for my new blog called Turning Over New Leaves.

I'm not an alcoholic. I certainly don't think I am, and I'm fairly certain that if you spoke to my friends and family they would agree that I don't have any issues with substance abuse. I definitely enjoy a drink. A few beers, gin and tonic's or a nice red wine (along with a few cigarettes) have been particular vices for the last few years of my life.

But no more. I'm going 365 with no alcohol and I am giving up cigarettes.

Why? I have my reasons... and this blog will reveal those and chronicle my year long journey.

The blog is called Turning Over New Leaves and I want a clean, crisp design to reflect this new adventure.

I'm looking for a design that is unique and not the same as every other blog you see. I want my readers to feel uplifted when they see it.

Most importantly, the blog needs to be simple for me to use and modify (add a new page if needed in the future)
Updates

Reason: To allow time for designers to submit revised designs.

Reason: My apologies designers, I haven't had an opportunity to provide feedback to enable changes. I will be doign this tomorrow morning and so am extending the deadline to allow resubmission.

Regards, Dale.

Target Market(s)

My target market are males and females, 17-28 in western speaking countries

Requirements
Must have
• - A graphic banner/branding featuring the blog title. This should be able to be used as a small stand alone logo.
- Ability to show my latest tweets
- A connect box where people can click on Chatterloop, Peepstream and Postvane links to contact me
- A widget that is showing how many days I am into the 365 day challenge (this should feature prominently)
- A widget that shows how much money as the challenge progresses
- It should have an ability to subcribe to the blog (RSS feeds)
- There needs to be an about me page
- There should be a blog roll
- There should be a list of categories/tags displayed somewhere (do something creative with this, find a way to make what I am talking about most more prominent!)
- A recent post link box somewhere at the side to encourage people to keep reading
- Recent comment links
- A search functionality
- An advertisement side bar (only a small amount of advertising will be done - so don't make it too prominent!)

Nice to have
• Without crowding the design it would also be good to have
-Popular post links (the most highly trafficked or commented) posts.

I'm excited to hear what other things YOU THINK should feature. Surprise me! I will reward innovation.

```html
<!DOCTYPE html>
<html lang="en">
<head>
<meta charset="utf-8">
<title>Turning Over New Leaves</title>
<link rel="stylesheet" href="https://fonts.googleapis.com/css2?family=Arimo:wght@400;700&family=Nothing+You+Could+Do&family=Gochi+Hand&display=swap">
<style>
  :root {
    --header-bg: #2e2b27;
    --sky-top: #a9dcf8;
    --sky-bottom: #d8f0fc;
    --paper: #ffffff;
    --sidebar: #f1f1f1;
    --ink: #111111;
    --body-text: #555555;
    --muted: #8a8a8a;
    --rule: #c9c9c9;
    --quote-bg: #f3f3f3;
    --leaf: #8cd12a;
    --leaf-dark: #4f8e10;
    --digit-dark: #2f2f2f;
    --tab-bg: #c8c8c8;
    --link-green: #8fb34a;
  }
  * { box-sizing: border-box; margin: 0; padding: 0; }
  html, body { width: 1200px; height: 1069px; overflow: hidden; }
  body {
    position: relative;
    font-family: "Arimo", Arial, sans-serif;
    background: linear-gradient(180deg, var(--sky-top) 0%, var(--sky-bottom) 100%);
  }
  .site-header {
    position: absolute; left: 0; top: 0; width: 1200px; height: 83px;
    background: var(--header-bg);
  }
  .site-header .zigzag { position: absolute; left: 0; top: 83px; }
  .brand {
    position: absolute; left: 178px; top: 22px;
    font-size: 27px; color: #ffffff; letter-spacing: -0.3px;
  }
  .main-nav { position: absolute; left: 508px; top: 18px; display: flex; }
  .main-nav a {
    font-family: "Nothing You Could Do", cursive;
    color: #e9e9e9; font-size: 21px; text-decoration: none;
    height: 42px; line-height: 42px; padding: 0 17px; margin-right: 9px;
  }
  .main-nav a.current { background: var(--leaf); border-radius: 10px; color: #fff; padding: 0 30px; }

  .hero-frame {
    position: absolute; left: 148px; top: 109px; width: 905px; height: 327px;
    background: #f7f7f7;
  }
  .hero-photo {
    position: absolute; left: 18px; top: 14px; width: 872px; height: 297px;
    background: linear-gradient(180deg, #4f7fc4 0%, #9cc0e6 45%, #88b93a 62%, #6fa21c 100%);
  }

  .content {
    position: absolute; left: 146px; top: 455px; width: 644px; height: 614px;
    background: var(--paper);
  }
  .post-title { position: absolute; left: 31px; top: 38px; font-size: 21px; font-weight: 400; color: var(--ink); }
  .post-meta { position: absolute; left: 32px; top: 66px; font-size: 13px; color: var(--muted); }
  .post-meta a { color: var(--ink); text-decoration: none; }
  .comment-count { position: absolute; left: 565px; top: 40px; }
  .pull-quote {
    position: absolute; left: 30px; top: 100px; width: 595px; height: 80px;
    background: var(--quote-bg); padding: 21px 40px 0 45px;
    font-size: 13.5px; line-height: 20px; color: var(--body-text);
  }
  .pull-quote::before {
    content: "\201C"; position: absolute; left: 18px; top: 10px;
    font-size: 40px; font-weight: 700; color: var(--ink); line-height: 1;
  }
  .post-body { position: absolute; left: 30px; top: 204px; width: 600px; }
  .post-body p { font-size: 13.3px; line-height: 19.8px; color: var(--body-text); margin-bottom: 6px; }
  .post-figure {
    position: absolute; left: 30px; top: 335px; width: 595px; height: 290px;
    background: #f4f4f4; padding: 5px;
  }
  .post-figure .photo {
    width: 586px; height: 285px;
    background: linear-gradient(90deg, #d9a98f 0%, #1a1a1c 25%, #0b0e16 100%);
  }

  .sidebar {
    position: absolute; left: 790px; top: 455px; width: 262px; height: 614px;
    background: var(--sidebar);
  }
  .search-box {
    position: absolute; left: 19px; top: 37px; width: 216px; height: 39px;
    background: #fff; border: 1px solid var(--rule);
  }
  .search-box svg { position: absolute; right: 10px; top: 12px; }
  .rule { position: absolute; left: 19px; width: 216px; height: 1px; background: var(--rule); }
  .widget-title { position: absolute; left: 19px; font-size: 17px; color: var(--muted); letter-spacing: 0.2px; }
  .counter { position: absolute; left: 19px; top: 143px; display: flex; gap: 4px; }
  .counter span {
    width: 51px; height: 51px; border-radius: 5px;
    background: linear-gradient(180deg, #4a4a4a 0%, var(--digit-dark) 50%, #1d1d1d 50%, #2b2b2b 100%);
    color: #fff; font-size: 42px; font-weight: 700; text-align: center; line-height: 51px;
  }
  .savings { position: absolute; left: 19px; top: 231px; display: flex; align-items: flex-end; gap: 3px; }
  .savings .currency { font-size: 30px; font-weight: 700; color: #333; line-height: 35px; margin-right: 2px; }
  .savings .digit {
    width: 35px; height: 35px; border-radius: 4px;
    background: linear-gradient(180deg, #a5e03f 0%, var(--leaf) 50%, #6db11a 50%, var(--leaf-dark) 100%);
    color: #fff; font-size: 29px; font-weight: 700; text-align: center; line-height: 35px;
  }
  .savings .dot { font-size: 26px; font-weight: 700; color: #333; line-height: 30px; }
  .post-tabs {
    position: absolute; left: 19px; top: 308px; width: 216px; height: 188px;
    background: #fff; border: 1px solid var(--rule);
  }
  .post-tabs .tabs { display: flex; height: 30px; }
  .post-tabs .tab { width: 50%; text-align: center; line-height: 30px; font-size: 15px; font-weight: 700; color: #c4c4c4; background: #f6f6f6; }
  .post-tabs .tab.active { background: var(--tab-bg); color: #fff; }
  .post-tabs ul { list-style: none; padding: 6px 8px 0 9px; }
  .post-tabs li {
    font-size: 12px; color: var(--muted); height: 25px; line-height: 22px;
    border-bottom: 1px dotted #aaa;
  }
  .post-tabs li:last-child { border-bottom: none; }
  .comment-card {
    position: absolute; left: 19px; top: 548px; width: 216px; height: 62px;
    background: #fff; border: 1px solid var(--rule); padding: 9px 8px;
  }
  .comment-card .avatar { position: absolute; left: 9px; top: 9px; width: 42px; height: 42px; background: linear-gradient(135deg, #cfcfcf, #7c7c7c); }
  .comment-card .text { position: absolute; left: 59px; top: 9px; font-size: 11.5px; line-height: 14.5px; color: #aaa; }
  .comment-card .text a { color: var(--link-green); text-decoration: none; }
  .comment-card .text small { font-size: 9px; color: #666; }

  .connect { position: absolute; left: 1055px; top: 455px; width: 140px; }
  .connect .label { font-family: "Gochi Hand", cursive; font-size: 15px; color: #666; margin-left: 6px; }
  .connect .arrow { margin: 2px 0 4px 30px; display: block; }
  .connect a {
    display: flex; align-items: center; gap: 5px; height: 52px; margin-bottom: 5px;
    font-size: 11px; color: #4a6a8a; text-decoration: none;
  }
  .connect a .chip { width: 44px; height: 48px; border-radius: 3px; flex: none; }
  .chip.blue { background: #8aa4d2; }
  .chip.sky { background: #7fc3de; }
  .chip.red { background: #c98585; }
</style>
</head>
<body>
  <header class="site-header">
    <div class="brand">Turning Over New Leaves</div>
    <nav class="main-nav">
      <a class="current" href="#">Home</a>
      <a href="#">About</a>
      <a href="#">Articles</a>
      <a href="#">Contact Me</a>
    </nav>
    <svg class="zigzag" width="1200" height="8" viewBox="0 0 1200 8" aria-hidden="true">
      <pattern id="teeth" width="12" height="8" patternUnits="userSpaceOnUse">
        <polygon points="0,0 12,0 6,8" fill="#2e2b27"/>
      </pattern>
      <rect width="1200" height="8" fill="url(#teeth)"/>
    </svg>
  </header>

  <div class="hero-frame">
    <div class="hero-photo" role="img" aria-label="Three people leaping joyfully across a green meadow under a blue cloudy sky"></div>
  </div>

  <main class="content">
    <h1 class="post-title">Dangerous Effects of Cigarette Smoking</h1>
    <p class="post-meta">in <a href="#">Smoking</a> tagged <a href="#">Health</a>, <a href="#">Bad Habit</a> on Nov 24th, 2009</p>
    <svg class="comment-count" width="52" height="40" viewBox="0 0 52 40" aria-label="10 comments">
      <ellipse cx="26" cy="16" rx="26" ry="16" fill="#111"/>
      <polygon points="30,28 40,38 38,26" fill="#111"/>
      <text x="26" y="21" text-anchor="middle" font-family="Arimo, sans-serif" font-size="13" font-weight="700" fill="#fff">10</text>
    </svg>
    <blockquote class="pull-quote">People who smoke a pack a day die on average 7 years earlier than people who have never smoked.</blockquote>
    <div class="post-body">
      <p>Cigarette Smoking means you are giving to yourself a slow poison treatment. Cigarette smoking does not only affect the smoker’s health but also affects the nearby standing individual like your kids as their organs are on developing stage.</p>
      <p>Some people are under false impression and take cigarette smoking as a hobby. According to recent studies conducted by Northfield Medical Board, Harbor Cancer Trust and the Clearbreath Lung and Heart Alliance, cigarette smoking is one of the main causes of premature death.</p>
    </div>
    <figure class="post-figure">
      <div class="photo" role="img" aria-label="Close-up of a lit cigarette held in the lips being cut by a pair of scissors, against a dark background with drifting smoke"></div>
    </figure>
  </main>

  <aside class="sidebar">
    <div class="search-box">
      <svg width="14" height="14" viewBox="0 0 14 14" aria-hidden="true">
        <circle cx="5.5" cy="5.5" r="4.3" fill="none" stroke="#bbb" stroke-width="2"/>
        <line x1="8.7" y1="8.7" x2="13" y2="13" stroke="#bbb" stroke-width="2.4"/>
      </svg>
    </div>
    <div class="rule" style="top:97px"></div>
    <h2 class="widget-title" style="top:112px">DAYS WITHOUT ALCOHOL</h2>
    <div class="counter"><span>3</span><span>6</span><span>5</span></div>
    <h2 class="widget-title" style="top:202px">Equal with</h2>
    <div class="savings">
      <span class="currency">$</span>
      <span class="digit">2</span><span class="digit">0</span><span class="digit">5</span>
      <span class="dot">.</span>
      <span class="digit">5</span>
    </div>
    <div class="rule" style="top:284px"></div>
    <section class="post-tabs">
      <div class="tabs"><span class="tab">Popular Post</span><span class="tab active">Recent Post</span></div>
      <ul>
        <li>Say no to smoking</li>
        <li>Making life more healthy</li>
        <li>Say no to smoking</li>
        <li>Making life more healthy</li>
        <li>Say no to smoking</li>
        <li>Making life more healthy</li>
      </ul>
    </section>
    <h2 class="widget-title" style="top:516px; font-size:16px; font-weight:700; color:#8c8c8c;">Recent Comments</h2>
    <div class="comment-card">
      <div class="avatar" role="img" aria-label="Commenter avatar"></div>
      <div class="text"><a href="#">Re: Say no to smoking</a><br>I agree with you dude...<br><small>Posted on 01-01-2010</small></div>
    </div>
  </aside>

  <nav class="connect">
    <div class="label">join me on</div>
    <svg class="arrow" width="14" height="26" viewBox="0 0 14 26" aria-hidden="true">
      <path d="M8 1 C7 9 7 16 6 24 M1 17 L6 24 L12 18" fill="none" stroke="#777" stroke-width="1.8" stroke-linecap="round"/>
    </svg>
    <a href="#"><span class="chip blue"></span>Chatterloop</a>
    <a href="#"><span class="chip sky"></span>Peepstream</a>
    <a href="#"><span class="chip red"></span>Postvane</a>
  </nav>
</body>
</html>
```